IT Company needs stationary design

Business cards, MS Word, PowerPoint, A4 notepad design base on our company logo. This must be a set of templates in the same style which could be used both for printable documents as well as for documents shared digitally via email, website etc. This should be a modern design which is still professional, so make sure content is well readable both in MS Word and MS PowerPoint templates.

Target Market(s)

SME and Corporate

Industry/Entity Type

It Company

Font styles to use
Sans Serif

Colors
0455a3
0692cd
f37122
ffc214

Requirements
Must have
• 1) Business cards design: modern but still professional
• 2) MS Word: mostly for IT project documents (business analysis, reports, specifications, etc.) must be professional and easy readable.
• 3) MS PowerPoint: first slide, normal slide, last slide.
• 4) A4 notepad: header (must), footer (must), some light design on the background (optionally)
Nice to have
• Business cards design: would be nice to have 2-4 color variations of the same design from one side - cover (for example part of the cards are blue, part of the cards are orange) and other side with contact details is identical.

```html
<!DOCTYPE html>
<html lang="en">
<head>
<meta charset="utf-8">
<title>Business Card – Cortavia</title>
<link rel="stylesheet" href="https://fonts.googleapis.com/css2?family=Quicksand:wght@300;400;500&display=swap">
<style>
  :root {
    --frame-grey: #d2d9d6;
    --card-dark: #151a1a;
    --card-light: #ffffff;
    --stripe-aqua: #7fe3dc;
    --stripe-yellow: #f5b80f;
    --stripe-orange: #f35a12;
    --text-light: #ffffff;
    --text-dark: #1a1a1a;
  }
  html, body {
    margin: 0;
    padding: 0;
    width: 1200px;
    height: 720px;
    overflow: hidden;
    background: var(--frame-grey);
    font-family: "Quicksand", sans-serif;
  }
  .card {
    position: absolute;
    left: 40px;
    top: 37px;
    width: 1120px;
    height: 640px;
    background: var(--card-light);
    overflow: hidden;
  }
  .card-background {
    position: absolute;
    inset: 0;
    width: 100%;
    height: 100%;
    display: block;
  }
  .holder {
    position: absolute;
    right: 51px;
    top: 50px;
    text-align: right;
    color: var(--text-light);
  }
  .holder-name {
    margin: 0;
    font-weight: 300;
    font-size: 84px;
    line-height: 1;
    letter-spacing: 0.5px;
  }
  .holder-role {
    margin: 14px 4px 0 0;
    font-weight: 400;
    font-size: 32px;
    line-height: 1;
  }
  .brand {
    position: absolute;
    left: 73px;
    top: 385px;
    display: flex;
    align-items: center;
    gap: 24px;
  }
  .brand-mark {
    width: 128px;
    height: 128px;
    box-sizing: border-box;
    border: 8px solid var(--text-dark);
    border-radius: 50%;
  }
  .brand-name {
    font-weight: 400;
    font-size: 70px;
    line-height: 1;
    color: var(--text-dark);
    padding-bottom: 10px;
  }
</style>
</head>
<body>
  <div class="card">
    <svg class="card-background" viewBox="0 0 1050 600" preserveAspectRatio="none" aria-hidden="true">
      <polygon class="dark-field" points="0,0 1050,0 1050,600 974,600 0,70" fill="var(--card-dark)"/>
      <polygon class="stripe stripe-aqua" points="0,70 974,600 0,78" fill="var(--stripe-aqua)"/>
      <polygon class="stripe stripe-yellow" points="0,78 974,600 0,88" fill="var(--stripe-yellow)"/>
      <polygon class="stripe stripe-orange" points="0,88 974,600 0,100" fill="var(--stripe-orange)"/>
    </svg>

    <div class="holder">
      <h1 class="holder-name">Your Name</h1>
      <p class="holder-role">Designation</p>
    </div>

    <div class="brand">
      <span class="brand-mark" aria-hidden="true"></span>
      <span class="brand-name">Cortavia</span>
    </div>
  </div>
</body>
</html>
```